Brightwell Rx Pass reinvent our website.

Our Website is outdated and needs an overhaul, in every aspect. We assist individuals that have little or no prescription coverage and allow them to receive a discount ranging from 33% up to 78% for free. In the beginning we utilized pharmacies to spread the word, but times have a changed. We are looking for a modern and clean site. We are open to anything, image, logo etc.

Target Market(s)

Anyone regardless of residency, age or income. This program is designed to assist those that have NO prescription coverage or for those whose particular prescription may not be covered by insurance.

Industry/Entity Type

Pharmaceutical

Coding

Coded - Design and coding required

Number of Pages Required

4 page

Requirements
Must have
• -The two MUST haves are the pharmacy locators & drug pricing. If you can combine the 2, even better.
• -a ongoing counter/tally on the 1stpage reflecting the amount of money we are saving customers. http://plumtreemarket.example/item/animated-counters-v-20-edge-animate-collection/full_screen_preview/52970314
• -on a smart phone the ability to view the information that is needed to get the actual discount for the medication.
Nice to have
• animated tutorial showing how to use the card
• health blog

```html
<!DOCTYPE html>
<html lang="en">
<head>
<meta charset="utf-8">
<title>Brightwell Rx Pass</title>
<link href="https://fonts.googleapis.com/css2?family=Montserrat:wght@400;600;700&family=Open+Sans:wght@400;600;700&display=swap" rel="stylesheet">
<style>
:root{
  --blue:#1b5e9f;
  --blue-deep:#134a80;
  --graphite:#3e3f41;
  --ink:#333;
  --paper:#f3f3f3;
  --muted:#b7b7b7;
  --red:#e5262b;
  --footer:#222224;
  --white:#fff;
}
*{box-sizing:border-box;margin:0;padding:0}
html,body{width:1200px;height:1025px;overflow:hidden}
body{position:relative;background:var(--blue);font-family:"Open Sans",sans-serif;color:var(--white)}
.backdrop{position:absolute;inset:0}
.partners{position:absolute;top:26px;left:0;width:1200px;text-align:center;color:var(--ink)}
.partners h2{font-family:"Montserrat",sans-serif;font-weight:700;font-size:20px;letter-spacing:1px}
.partners p{font-size:11px;color:#777;margin-top:4px}
.partner-row{display:flex;justify-content:center;gap:74px;margin-top:24px}
.partner-name{font-family:"Open Sans",sans-serif;font-weight:600;font-size:17px;color:var(--muted);display:flex;align-items:center;gap:7px}
.partner-name i{width:9px;height:9px;background:var(--muted);border-radius:50%;display:inline-block}
.finder{position:absolute;top:170px;left:170px;width:720px;color:var(--ink)}
.finder h3{font-family:"Montserrat",sans-serif;font-weight:700;font-size:17px;letter-spacing:1px}
.finder .lead{font-size:12px;color:#555;margin-top:5px}
.finder-form{display:flex;gap:10px;margin-top:16px}
.field{height:38px;border:1px solid #ddd;background:var(--white);font-size:12px;color:#999;padding:11px 12px}
.field.drug{width:200px}.field.zip{width:150px}.field.radius{width:130px}
.search-btn{height:38px;padding:0 22px;background:var(--red);color:var(--white);border:none;font-family:"Montserrat",sans-serif;font-weight:600;font-size:12px;letter-spacing:1px}
.note{margin-top:10px;font-size:11px;color:var(--red);display:flex;align-items:center;gap:6px}
.features-title{position:absolute;top:494px;left:60px}
.features-title h2{font-family:"Montserrat",sans-serif;font-weight:700;font-size:30px;line-height:36px;letter-spacing:4px}
.features-title p{font-family:"Montserrat",sans-serif;font-size:12px;letter-spacing:2px;color:var(--red);margin-top:2px}
.step{position:absolute;width:200px;text-align:left}
.step .badge{width:120px;height:120px;border-radius:50%;background:var(--blue-deep);display:flex;align-items:center;justify-content:center}
.step h4{font-family:"Montserrat",sans-serif;font-weight:700;font-size:12px;margin-top:14px;letter-spacing:.5px}
.step p{font-size:11px;line-height:1.45;opacity:.9;margin-top:4px;width:160px}
.clients{position:absolute;top:770px;left:620px}
.clients h2{font-family:"Montserrat",sans-serif;font-weight:600;font-size:26px}
.clients p{font-size:12px;opacity:.8;margin-top:3px}
.portrait{position:absolute;border-radius:50%;background:radial-gradient(circle at 50% 40%,#d9b9a2,#8a6f60 70%,#4a4a4c)}
.footer{position:absolute;top:905px;left:0;width:1200px;height:120px;background:var(--footer);padding:26px 60px;display:flex;justify-content:space-between}
.copyright{font-size:11px;color:#999;line-height:1.6}
.copyright b{color:var(--red);font-weight:600}
.cards{display:flex;gap:8px;margin-top:12px}
.cards span{width:32px;height:20px;background:#555;border-radius:3px}
.newsletter{text-align:right}
.newsletter label{font-family:"Montserrat",sans-serif;font-size:11px;letter-spacing:1px;color:#ccc}
.subscribe{display:flex;margin-top:8px;justify-content:flex-end}
.subscribe .email{width:220px;height:32px;border:1px solid #555;font-size:11px;color:#888;padding:8px 10px}
.subscribe .go{height:32px;padding:0 16px;background:var(--red);color:var(--white);border:none;font-size:10px;font-weight:700;letter-spacing:1px}
.footer-nav{display:flex;gap:22px;justify-content:flex-end;margin-top:10px;font-size:11px;color:#ddd}
</style>
</head>
<body>
<svg class="backdrop" width="1200" height="1025" viewBox="0 0 1200 1025" aria-hidden="true">
  <path d="M0 400 C0 440 90 470 220 474 C420 480 590 470 720 370 C840 280 950 180 1200 150 L1200 200 C1000 230 880 340 760 470 C660 580 520 610 300 610 L0 610 Z" fill="var(--graphite)"/>
  <path d="M0 0 H1200 V150 C950 180 840 280 720 370 C590 470 420 480 220 474 C90 470 0 440 0 400 Z" fill="var(--paper)"/>
  <path d="M1200 560 C1040 590 940 640 860 720 C760 820 620 890 420 905 L1200 905 Z" fill="var(--graphite)"/>
  <g stroke="#fff" stroke-width="1.5" stroke-dasharray="5 5" fill="none">
    <path d="M120 580 H190 L250 550 H440 L500 500 H690 L750 440 H940 L1000 400 H1080"/>
  </g>
  <g font-family="Montserrat, sans-serif" font-size="10" font-weight="700" text-anchor="middle">
    <circle cx="190" cy="580" r="11" fill="#fff"/><text x="190" y="584" fill="var(--blue)">1</text>
    <circle cx="440" cy="550" r="11" fill="#fff"/><text x="440" y="554" fill="var(--blue)">2</text>
    <circle cx="690" cy="500" r="11" fill="#fff"/><text x="690" y="504" fill="var(--blue)">3</text>
    <circle cx="940" cy="440" r="11" fill="#fff"/><text x="940" y="444" fill="var(--blue)">4</text>
  </g>
  <rect x="596" y="800" width="8" height="8" fill="var(--red)" transform="rotate(45 600 804)"/>
  <rect x="1156" y="716" width="8" height="8" fill="var(--red)" transform="rotate(45 1160 720)"/>
</svg>

<section class="partners">
  <h2>OUR PARTNERS</h2>
  <p>Be a our partner to save on medication bills!</p>
  <div class="partner-row">
    <span class="partner-name"><i></i>Kestrel</span>
    <span class="partner-name">Arclight</span>
    <span class="partner-name">Lumora</span>
    <span class="partner-name">Fernway</span>
    <span class="partner-name"><i></i>Tunewell</span>
    <span class="partner-name">Swiftmark</span>
  </div>
</section>

<section class="finder">
  <h3>SEARCH A PHARMACY &amp; DRUG PRICE NOW?</h3>
  <p class="lead">Enter your Drug Name, zip code and get price of drug along with location of pharmacy!</p>
  <div class="finder-form">
    <div class="field drug">Drug Name</div>
    <div class="field zip">ZIP CODE</div>
    <div class="field radius">Within ... km</div>
    <button class="search-btn">Search Pharmacy</button>
  </div>
  <p class="note">
    <svg width="10" height="13" viewBox="0 0 10 13" aria-hidden="true"><path d="M5 0 C2 0 0 2 0 5 C0 8 5 13 5 13 C5 13 10 8 10 5 C10 2 8 0 5 0 Z" fill="var(--red)"/><circle cx="5" cy="5" r="2" fill="#fff"/></svg>
    * Enter the radious in kilometer in which you want to locate the pharmacy
  </p>
</section>

<header class="features-title">
  <h2>FEATURES</h2>
  <p>SAVING YOUR MEDICATIONS</p>
</header>

<article class="step" style="left:130px;top:600px">
  <div class="badge"><svg width="70" height="62" viewBox="0 0 70 62" aria-hidden="true"><path d="M18 0 H52 L70 31 L52 62 H18 L0 31 Z" fill="#fff"/><rect x="22" y="20" width="26" height="20" rx="2" fill="none" stroke="var(--blue)" stroke-width="2"/><rect x="22" y="25" width="26" height="4" fill="var(--blue)"/></svg></div>
  <h4>GET YOUR FREE CARD</h4>
  <p>amet, consectetur adipisicing elit, sed do eiusmod tempor incididunt</p>
</article>
<article class="step" style="left:380px;top:568px">
  <div class="badge"><svg width="70" height="62" viewBox="0 0 70 62" aria-hidden="true"><path d="M18 0 H52 L70 31 L52 62 H18 L0 31 Z" fill="#fff"/><circle cx="28" cy="22" r="5" fill="var(--blue)"/><circle cx="43" cy="22" r="5" fill="var(--blue)"/><rect x="23" y="29" width="10" height="14" fill="var(--blue)"/><rect x="38" y="29" width="10" height="14" fill="var(--blue)"/></svg></div>
  <h4>HOW IT WORKS</h4>
  <p>amet, consectetur adipisicing elit, sed do eiusmod tempor incididunt</p>
</article>
<article class="step" style="left:630px;top:518px">
  <div class="badge"><svg width="70" height="62" viewBox="0 0 70 62" aria-hidden="true"><path d="M18 0 H52 L70 31 L52 62 H18 L0 31 Z" fill="#fff"/><rect x="22" y="34" width="26" height="10" fill="var(--blue)"/><circle cx="37" cy="20" r="5" fill="var(--blue)"/><rect x="33" y="26" width="8" height="8" fill="var(--blue)"/></svg></div>
  <h4>CREATE YOUR CARD</h4>
  <p>amet, consectetur adipisicing elit, sed do eiusmod tempor incididunt</p>
</article>
<article class="step" style="left:880px;top:458px">
  <div class="badge"><svg width="70" height="62" viewBox="0 0 70 62" aria-hidden="true"><path d="M18 0 H52 L70 31 L52 62 H18 L0 31 Z" fill="#fff"/><rect x="24" y="18" width="22" height="18" fill="none" stroke="var(--blue)" stroke-width="2"/><rect x="28" y="22" width="14" height="3" fill="var(--blue)"/><rect x="33" y="36" width="4" height="8" fill="var(--blue)"/></svg></div>
  <h4>JOIN US</h4>
  <p>amet, consectetur adipisicing elit, sed do eiusmod tempor incididunt</p>
</article>

<section class="clients">
  <h2>Clients Says</h2>
  <p>What our clients are saying about us?</p>
</section>
<div class="portrait" role="img" aria-label="Portrait of a smiling client" style="left:440px;top:800px;width:90px;height:90px"></div>
<div class="portrait" role="img" aria-label="Portrait of a client wearing glasses" style="left:1080px;top:600px;width:80px;height:80px"></div>

<footer class="footer">
  <div>
    <p class="copyright">Copyrights © <b>Brightwell Rx Pass</b> 2015.<br>All rights reserved</p>
    <div class="cards"><span></span><span></span><span></span><span></span></div>
  </div>
  <div class="newsletter">
    <label>SUBSCRIBE to OUR NEWS LETTER</label>
    <div class="subscribe"><div class="email">Enter Your Email Address</div><button class="go">SUBSCRIBE</button></div>
    <nav class="footer-nav"><span>Home</span><span>About us</span><span>Terms &amp; Conditions</span><span>Contact</span></nav>
  </div>
</footer>
</body>
</html>
```